Business card design needed

Our modern electrical contracting company requires business card design utilising our logo and incorporating our tag line "Service when you need it". We specialise in assisting our customers 24/7 offering a breakdown service.

Industry/Entity Type

Electrical

Contact Information for Business Card

Marcus Penhale, Electrical contractor,Tel: (08) 8456 3071, Fax: (08) 8679 4315, Mob 0438 562 740, Email: marcus.penhale@brightwirepower.com.au, Web: www.brightwirepower.com.au

Requirements
Must have
• we require a 2 sided card.
Front- Logo, tag line and contact information.
Rear- service when you need it! Call now for our 24/7 breakdown service

```html
<!DOCTYPE html>
<html lang="en">
<head>
<meta charset="utf-8">
<title>Breakdown Service Card – Rear</title>
<link href="https://fonts.googleapis.com/css2?family=Arimo:wght@400;700&family=Source+Sans+3:wght@600&display=swap" rel="stylesheet">
<style>
  :root {
    --bg-cyan: #2ff2f2;
    --bg-light: #b8fbfb;
    --bg-white: #ffffff;
    --ink: #111111;
    --accent-red: #ff1a0d;
    --disc-light: #c9f8fd;
    --disc-mid: #5fd6fb;
    --disc-deep: #1f6fec;
  }
  html, body {
    margin: 0;
    padding: 0;
    width: 1200px;
    height: 676px;
    overflow: hidden;
  }
  .card {
    position: relative;
    width: 1200px;
    height: 676px;
    overflow: hidden;
    background:
      radial-gradient(ellipse 720px 620px at 1200px 120px, var(--bg-white) 0%, var(--bg-light) 45%, rgba(184,251,251,0) 80%),
      linear-gradient(90deg, var(--bg-cyan) 0%, #5ff6f6 55%, #a8fbfb 100%);
  }
  .tagline {
    position: absolute;
    right: 603px;
    top: 301px;
    margin: 0;
    text-align: right;
    font-family: "Arimo", Arial, sans-serif;
    color: var(--ink);
    line-height: 1;
  }
  .tagline__lead {
    display: block;
    font-size: 36px;
    font-weight: 400;
    letter-spacing: -0.3px;
  }
  .tagline__cta {
    display: block;
    margin-top: 8px;
    font-size: 36px;
    font-weight: 700;
    letter-spacing: -0.2px;
  }
  .hours {
    position: absolute;
    left: 625px;
    top: 268px;
    margin: 0;
    font-family: "Arimo", Arial, sans-serif;
    font-weight: 700;
    font-size: 136px;
    line-height: 1;
    letter-spacing: -2px;
    color: var(--accent-red);
    z-index: 2;
  }
  .service-badge {
    position: absolute;
    left: 0;
    top: 0;
    width: 1200px;
    height: 676px;
    z-index: 1;
  }
  .service-badge__label {
    font-family: "Source Sans 3", "Myriad Pro", sans-serif;
    font-weight: 600;
    font-size: 34px;
    fill: var(--ink);
  }
</style>
</head>
<body>
  <main class="card">
    <svg class="service-badge" viewBox="0 0 1200 676">
      <defs>
        <radialGradient id="discTone" cx="0.5" cy="0.45" r="0.6">
          <stop offset="0" stop-color="var(--disc-light)"/>
          <stop offset="0.6" stop-color="var(--disc-mid)"/>
          <stop offset="1" stop-color="var(--disc-deep)"/>
        </radialGradient>
        <path id="labelArc" d="M762 220 A150 150 0 1 1 870.7 496.2"/>
      </defs>
      <circle cx="837" cy="350" r="124" fill="url(#discTone)" opacity="0.55" role="img" aria-label="Decorative round badge area behind the 24/7 hours"/>
      <text class="service-badge__label" aria-hidden="false">
        <textPath href="#labelArc">offering a breakdown service</textPath>
      </text>
    </svg>

    <p class="tagline">
      <span class="tagline__lead">service when you need it!</span>
      <span class="tagline__cta">Call now for our</span>
    </p>
    <p class="hours">24/7</p>
  </main>
</body>
</html>
```